Information Technology Company needs a Website...

We need a single page website for new technology company called:

MERIDEL FALLS TECHNOLOGY GROUP
Based in Ojai CA.

We are offering three primary services:

- Business Solutions

- IT Services

- Software Implementation and Consulting

We want a single page design where all content scrolls down/up on one page. We're looking for the following characteristics:

- Home/Landing
- Active background with panoramic view (Will provide content)

- Business Solutions, IT Services, Software Implementation and Consulting

List of software vendors we recommend (Company logos)

- About
- History
- Our Team
- Partners

I'll upload our new logo as soon as we get the design files. I'll also send over some example website layout's that we like shortly.

Target Market(s)

Small/Medium Businesses

Industry/Entity Type

Information Technology

Number of Pages Required

1 page

Font styles to use
Other font styles liked:
• Sansation

Requirements
Must have
• Full page browser width, easy navigation and visibility. Creative design, not like every other "Technology" website template. Should be the "One Page" design where each section is below the next and the user scrolls down the page through the whole site. I like the concept of the following website in the main "Whiteboard" image:
• http://www.plavorix.com/design/4829137
• And the way this site does the active panoramic background:
• http://www.kelbrantworks.com/
• Something interesting and appealing to potential clients looking for Small/Medium business solutions and IT Services.
• Use uploaded Logo to establish color and theme for website.
Should not have
• Look the same as every other information technology website template.

```html
<!DOCTYPE html>
<html lang="en">
<head>
<meta charset="utf-8">
<title>Meridel Falls Technology Group</title>
<link rel="stylesheet" href="https://fonts.googleapis.com/css2?family=Open+Sans:ital,wght@0,400;0,600;0,700;0,800;1,400;1,700;1,800&display=swap">
<style>
:root{
  --orange:#f05423;
  --orange-deep:#e0481b;
  --charcoal:#454545;
  --ink:#2e2e2e;
  --panel:#262626;
  --light:#e7e7e7;
  --card:#c9c9c9;
  --footer:#151515;
  --white:#ffffff;
  --green:#8dc63f;
  --muted:#9a9a9a;
}
*{margin:0;padding:0;box-sizing:border-box}
html,body{width:1200px;height:3279px;overflow:hidden}
body{position:relative;font-family:"Open Sans",Arial,sans-serif;color:var(--white);background:var(--light)}
.abs{position:absolute}
ul{list-style:none}

/* nav */
.main-nav{position:absolute;left:269px;top:0;width:693px;height:61px;background:var(--orange);border-radius:0 0 14px 14px;box-shadow:0 4px 10px rgba(0,0,0,.35);z-index:5;display:flex;align-items:center;justify-content:space-around;padding:0 18px}
.main-nav a{color:var(--white);text-decoration:none;font-size:16px;padding:8px 12px}
.main-nav a.active{background:rgba(255,255,255,.22);border-radius:3px}

/* hero */
.hero{left:0;top:0;width:1200px;height:700px;background:linear-gradient(180deg,#7f8196 0%,#9c97aa 22%,#c9a7ac 45%,#efc2ab 62%,#d8b2ac 68%,#8f95a6 74%,#737d91 100%)}
.brand{left:0;top:300px;width:1200px;text-align:center;color:var(--white);font-weight:600;font-size:40px;letter-spacing:1px;line-height:1}
.hero-note{left:0;top:480px;width:1200px;text-align:center;font-size:21px;color:rgba(255,255,255,.9)}
.hero-social{left:570px;top:617px;display:flex;gap:6px}
.hero-social span{width:22px;height:22px;border-radius:50%;background:var(--white)}

/* intro split */
.split{left:0;top:620px;width:1200px;height:882px}
.sec-head{display:flex;align-items:center;justify-content:center;gap:12px;font-weight:700;font-size:23px;letter-spacing:.5px}
.sec-head i{display:block;height:2px;width:70px;position:relative}
.sec-head i::before{content:"";position:absolute;top:-4px;width:10px;height:10px;border-radius:50%;background:inherit}
.sec-head i.l::before{left:-4px}
.sec-head i.r::before{right:-4px}
.about-head{left:100px;width:380px}
.about-head i{background:var(--white)}
.about-text{left:128px;width:390px;font-size:18px;line-height:29.5px}
.know-more{left:130px;top:1045px;display:flex;align-items:center;gap:10px;font-size:11px}
.circle-arrow{width:34px;height:34px;border:2px solid currentColor;border-radius:50%;display:flex;align-items:center;justify-content:center}
.services-head{left:700px;top:720px;width:360px}
.services-head i{background:var(--orange)}
.service{left:790px;width:206px;height:206px;border:3px solid var(--white);border-radius:50%;text-align:center;padding-top:34px}
.service h3{color:var(--orange);font-size:11px;font-weight:700;margin:6px auto 4px;width:130px;line-height:13px}
.service p{font-size:10px;line-height:12px;width:112px;margin:0 auto}
.view-more{left:1013px;width:54px;height:15px;border-radius:8px;background:var(--orange);font-size:8px;font-weight:700;text-align:center;line-height:15px}

/* team */
.team{left:0;top:1502px;width:1200px;height:505px;background:var(--light)}
.team-head{left:0;top:1520px;width:1200px;color:var(--ink)}
.team-head i{background:var(--orange)}
.member{top:1587px;width:212px;height:319px;background:var(--card);border-radius:10px;overflow:hidden;text-align:center;color:var(--ink)}
.member.featured{background:var(--white);border:2px solid #d0d0d0}
.photo{width:136px;height:136px;border-radius:50%;margin:18px auto 0;background:radial-gradient(circle at 50% 40%,#c98d70 0%,#9b5f49 45%,#b84a38 100%);border:3px solid #e07050}
.photo.alt{background:radial-gradient(circle at 50% 40%,#d9b08f 0%,#8f6346 55%,#6b4a33 100%);border-color:#d7c2b0}
.member h4{color:var(--orange);font-size:20px;font-weight:600;margin-top:10px;line-height:22px}
.member .role{font-size:12px;line-height:14px}
.member .bio{font-size:10.5px;font-weight:700;line-height:12.5px;width:160px;margin:10px auto 0}
.member-bar{position:absolute;left:0;bottom:0;width:100%;height:28px;background:#b5b5b5;display:flex;justify-content:center;align-items:center;gap:6px}
.member.featured .member-bar{background:var(--orange)}
.member-bar span{width:13px;height:13px;border-radius:50%;background:var(--white)}
.member-bar span.sq{border-radius:2px}
.pager{top:1701px;width:70px;height:70px;border-radius:50%;border:3px solid #d4d4d4;display:flex;align-items:center;justify-content:center}
.pager.next{border-color:var(--orange)}
.dots{left:556px;top:1954px;display:flex;gap:10px}
.dots span{width:16px;height:16px;border-radius:50%;background:#c4c4c4}
.dots span.on{background:var(--orange)}

/* news */
.news{left:0;top:2007px;width:1200px;height:573px;background:radial-gradient(ellipse at 55% 40%,#5a5a5a 0%,#3d3d3d 50%,#2b2b2b 100%)}
.news-title{left:138px;top:2042px;font-size:24px;font-weight:600}
.news-title b{color:var(--orange);font-weight:600}
.more-news{left:525px;top:2044px;display:flex;align-items:center;gap:8px;font-size:11px}
.more-news .circle-arrow{width:32px;height:32px}
.timeline-h{left:130px;top:2094px;width:486px;height:1px;background:var(--orange)}
.timeline-v{left:616px;top:2094px;width:1px;height:416px;background:var(--orange)}
.tl-dot{left:612px;width:9px;height:9px;border-radius:50%;background:var(--orange)}
.news-item{left:125px;width:426px;height:123px;background:rgba(28,28,28,.9);border-radius:10px}
.news-thumb{position:absolute;left:13px;top:14px;width:94px;height:94px;background:linear-gradient(180deg,#b8c4cc 0%,#a9a38f 50%,#5f7a44 100%)}
.news-body{position:absolute;left:135px;top:8px;width:280px}
.news-body h5{font-size:16px;font-weight:700;line-height:20px}
.news-meta{font-size:10.5px;color:#bbb}
.news-meta b{color:var(--orange);font-weight:600}
.news-body p{font-size:13.5px;line-height:17px;margin-top:4px}
.read-more{position:absolute;right:22px;bottom:4px;font-size:9px;color:#ccc}
.bubble{left:820px;top:2056px}
.quote-box{left:662px;top:2326px;width:385px;height:188px;background:rgba(30,30,30,.92);border-radius:12px}
.quote-text{left:712px;top:2336px;width:285px;font-size:14px;line-height:17px}
.qm{color:var(--orange);font-size:26px;font-weight:800;font-style:italic;line-height:0;vertical-align:-6px}
.quote-photo{left:715px;top:2405px;width:98px;height:98px;background:radial-gradient(circle at 50% 40%,#d8b8a0 0%,#8c6650 60%,#4d3a30 100%)}
.quote-name{left:830px;top:2434px;color:var(--orange);font-size:15px;font-weight:700}
.quote-role{left:830px;top:2456px;font-size:11px;font-style:italic}
.next-link{left:1078px;top:2388px;font-size:10px;text-align:center}
.next-link .circle-arrow{width:30px;height:30px;margin-top:3px}

/* partners */
.partners{left:0;top:2580px;width:1200px;height:251px;background:var(--light)}
.partners-head{left:0;top:2618px;width:1200px;color:var(--ink)}
.partners-head i{background:var(--orange)}
.partner{background:var(--muted)}

/* footer */
.footer{left:0;top:2831px;width:1200px;height:387px;background:var(--footer)}
.foot-h{top:2910px;color:var(--orange);font-size:15px;font-weight:700;letter-spacing:.3px}
.foot-line{font-size:14px;display:flex;align-items:center;gap:14px}
.foot-list li{font-size:14px;line-height:23.6px}
.news-input{left:863px;top:2997px;width:213px;height:22px;background:#bdbdbd;border-radius:2px;color:#777;font-size:12px;line-height:22px;padding-left:30px}
.subscribe{left:979px;top:3032px;width:97px;height:22px;background:var(--green);border-radius:2px;color:#2a3a10;font-size:13px;text-align:center;line-height:22px}
.bottom-bar{left:0;top:3218px;width:1200px;height:61px;background:var(--orange);text-align:center;font-size:11px;line-height:14px;padding-top:13px}
</style>
</head>
<body>

<div class="abs hero" role="img" aria-label="Panoramic photograph of a sunset sky over calm water and distant islands"></div>

<nav class="main-nav">
  <a class="active" href="#home">Home</a>
  <a href="#about">About</a>
  <a href="#history">History</a>
  <a href="#team">Our Team</a>
  <a href="#partners">Partners</a>
  <a href="#services">Services</a>
  <a href="#contact">Contact Us</a>
</nav>

<div class="abs brand">MERIDEL FALLS TECHNOLOGY GROUP</div>
<div class="abs hero-note">Panoramic image goes here</div>
<div class="abs hero-social"><span></span><span></span></div>

<svg class="abs split" width="1200" height="882" viewBox="0 0 1200 882">
  <defs>
    <linearGradient id="edgeShade" x1="0" x2="1">
      <stop offset="0.85" stop-color="#f05423"/>
      <stop offset="1" stop-color="#d0431a"/>
    </linearGradient>
  </defs>
  <path d="M600 48 Q900 -5 1200 50 L1200 882 L600 882 Z" fill="#454545"/>
  <path d="M0 55 Q320 -20 600 45 L600 882 L0 882 Z" fill="url(#edgeShade)"/>
</svg>

<div class="abs sec-head about-head" style="top:720px"><i class="l"></i>WHO WE ARE<i class="r"></i></div>
<p class="abs about-text" style="top:760px">Lorem Ipsum is simply dummy text of the printing and typesetting industry. Lorem Ipsum has been the industry's standard dummy text ever since the 1500s, when an unknown printer took a galley of type and scrambled it to make a type specimen book. It has survived not only five centuries, but also the leap into electronic typesetting, remaining essentially unchanged.</p>
<div class="abs know-more">Know More
  <span class="circle-arrow"><svg width="10" height="14" viewBox="0 0 10 14"><path d="M2 1l6 6-6 6" fill="none" stroke="#fff" stroke-width="2"/></svg></span>
</div>
<div class="abs sec-head about-head" style="top:1134px"><i class="l"></i>WHY CHOOSE US<i class="r"></i></div>
<p class="abs about-text" style="top:1196px">Lorem Ipsum is simply dummy text of the printing and typesetting industry. Lorem Ipsum has been the industry's standard dummy text ever since the 1500s, when an unknown printer took a galley of type and scrambled it to make a type specimen book. It has survived not only five centuries, but also the leap into electronic typesetting, remaining essentially unchanged.</p>

<div class="abs sec-head services-head"><i class="l"></i>OUR SERVICES<i class="r"></i></div>

<div class="abs service" style="top:785px">
  <svg width="40" height="34" viewBox="0 0 40 34"><rect x="6" y="3" width="28" height="20" rx="2" fill="none" stroke="#f05423" stroke-width="3"/><rect x="2" y="26" width="36" height="5" rx="2" fill="#f05423"/></svg>
  <h3>IT Services</h3>
  <p>Lorem Ipsum is simply dummy text of the printing and typesetting industry. Lorem Ipsum</p>
</div>
<div class="abs view-more" style="top:878px">View More</div>

<div class="abs service" style="top:1012px">
  <svg width="44" height="34" viewBox="0 0 44 34"><rect x="3" y="8" width="20" height="14" rx="4" fill="#f05423" transform="rotate(-20 13 15)"/><rect x="20" y="10" width="20" height="14" rx="4" fill="#f05423" transform="rotate(20 30 17)"/></svg>
  <h3>Business Solutions</h3>
  <p>Lorem Ipsum is simply dummy text of the printing and typesetting industry. Lorem Ipsum</p>
</div>
<div class="abs view-more" style="top:1106px">View More</div>

<div class="abs service" style="top:1239px">
  <svg width="40" height="40" viewBox="0 0 40 40"><circle cx="20" cy="20" r="13" fill="none" stroke="#f05423" stroke-width="6" stroke-dasharray="6 4"/><circle cx="20" cy="20" r="5" fill="#f05423"/></svg>
  <h3>Software Implementation &amp; Consulting</h3>
  <p>Lorem Ipsum is simply dummy text of the printing and typesetting industry. Lorem Ipsum</p>
</div>
<div class="abs view-more" style="top:1322px">View More</div>

<section class="abs team"></section>
<div class="abs sec-head team-head"><i class="l"></i>MEET OUR TEAM<i class="r"></i></div>

<div class="abs pager" style="left:41px">
  <svg width="18" height="28" viewBox="0 0 18 28"><path d="M15 2L3 14l12 12" fill="none" stroke="#d4d4d4" stroke-width="3"/></svg>
</div>
<div class="abs pager next" style="left:1086px">
  <svg width="18" height="28" viewBox="0 0 18 28"><path d="M3 2l12 12L3 26" fill="none" stroke="#333" stroke-width="3"/></svg>
</div>

<article class="abs member featured" style="left:131px">
  <div class="photo" role="img" aria-label="Team member portrait"></div>
  <h4>Name Here</h4><div class="role">Designation</div>
  <p class="bio">Loremipsumissimply dummy text of the printing andypesettingindustry. LoremIpsum has been the industry'standard dummy text ever</p>
  <div class="member-bar"><span class="sq"></span><span class="sq"></span><span></span><span></span></div>
</article>
<article class="abs member" style="left:374px">
  <div class="photo alt" role="img" aria-label="Team member portrait"></div>
  <h4>Name Here</h4><div class="role">Designation</div>
  <p class="bio">Loremipsumissimply dummy text of the printing andypesettingindustry. LoremIpsum has been the industry'standard dummy text ever</p>
  <div class="member-bar"><span class="sq"></span><span class="sq"></span><span></span><span></span></div>
</article>
<article class="abs member" style="left:610px">
  <div class="photo" role="img" aria-label="Team member portrait"></div>
  <h4>Name Here</h4><div class="role">Designation</div>
  <p class="bio">Loremipsumissimply dummy text of the printing andypesettingindustry. LoremIpsum has been the industry'standard dummy text ever</p>
  <div class="member-bar"><span class="sq"></span><span class="sq"></span><span></span><span></span></div>
</article>
<article class="abs member" style="left:846px">
  <div class="photo" role="img" aria-label="Team member portrait"></div>
  <h4>Name Here</h4><div class="role">Designation</div>
  <p class="bio">Loremipsumissimply dummy text of the printing andypesettingindustry. LoremIpsum has been the industry'standard dummy text ever</p>
  <div class="member-bar"><span class="sq"></span><span class="sq"></span><span></span><span></span></div>
</article>
<div class="abs dots"><span class="on"></span><span></span><span></span><span></span></div>

<section class="abs news" role="img" aria-label="Dark background with a faint network of connected points"></section>
<h2 class="abs news-title"><b>LATEST</b> NEWS</h2>
<div class="abs more-news">More News
  <span class="circle-arrow"><svg width="10" height="14" viewBox="0 0 10 14"><path d="M2 1l6 6-6 6" fill="none" stroke="#fff" stroke-width="2"/></svg></span>
</div>
<div class="abs timeline-h"></div>
<div class="abs timeline-v"></div>
<div class="abs tl-dot" style="top:2090px"></div>
<div class="abs tl-dot" style="top:2250px"></div>
<div class="abs tl-dot" style="top:2506px"></div>

<article class="abs news-item" style="top:2127px">
  <div class="news-thumb" role="img" aria-label="Photo of a house"></div>
  <div class="news-body"><h5>Ttitle Goes Here</h5><div class="news-meta"><b>Ellis</b> | 20/05/2016</div>
  <p>Lorem Ipsum is simply dummy text of the printing and typesetting industry. Lorem Ipsum has been the</p></div>
  <span class="read-more">Read More..</span>
</article>
<article class="abs news-item" style="top:2260px">
  <div class="news-thumb" role="img" aria-label="Photo of a house"></div>
  <div class="news-body"><h5>Ttitle Goes Here</h5><div class="news-meta"><b>Marlow</b> | 20/05/2016</div>
  <p>Lorem Ipsum is simply dummy text of the printing and typesetting industry. Lorem Ipsum has been the</p></div>
  <span class="read-more">Read More..</span>
</article>
<article class="abs news-item" style="top:2391px">
  <div class="news-thumb" role="img" aria-label="Photo of a house"></div>
  <div class="news-body"><h5>Ttitle Goes Here</h5><div class="news-meta"><b>Kessa</b> | 20/05/2016</div>
  <p>Lorem Ipsum is simply dummy text of the printing and typesetting industry. Lorem Ipsum has been the</p></div>
  <span class="read-more">Read More..</span>
</article>

<svg class="abs bubble" width="250" height="280" viewBox="0 0 250 280">
  <path d="M124 14a106 106 0 1 1 -40 205 L60 262 L64 205 A106 106 0 0 1 124 14Z" fill="#111" stroke="#f05423" stroke-width="9" stroke-linejoin="round"/>
  <text x="124" y="97" text-anchor="middle" fill="#fff" font-family="Open Sans, sans-serif" font-size="27" font-weight="800" font-style="italic">WHAT'S</text>
  <text x="124" y="131" text-anchor="middle" fill="#fff" font-family="Open Sans, sans-serif" font-size="27" font-weight="800" font-style="italic">PEOPLE</text>
  <text x="124" y="165" text-anchor="middle" fill="#f05423" font-family="Open Sans, sans-serif" font-size="27" font-weight="800" font-style="italic">SAYING?</text>
</svg>

<div class="abs quote-box"></div>
<p class="abs quote-text"><span class="qm">“</span> Lorem Ipsum is simply dummy text of the printing and typesetting industry. Lorem Ipsum has been the <span class="qm">”</span></p>
<div class="abs quote-photo" role="img" aria-label="Client portrait"></div>
<div class="abs quote-name">Rosalind Varga</div>
<div class="abs quote-role">Designation</div>
<div class="abs next-link">Next
  <span class="circle-arrow"><svg width="10" height="14" viewBox="0 0 10 14"><path d="M2 1l6 6-6 6" fill="none" stroke="#fff" stroke-width="2"/></svg></span>
</div>

<section class="abs partners"></section>
<div class="abs sec-head partners-head"><i class="l"></i>OUR PARTNERS<i class="r"></i></div>
<div class="abs partner" style="left:144px;top:2709px;width:62px;height:62px;border-radius:50%"></div>
<div class="abs partner" style="left:278px;top:2727px;width:134px;height:24px;border-radius:4px"></div>
<div class="abs partner" style="left:488px;top:2709px;width:60px;height:56px;border-radius:4px"></div>
<div class="abs partner" style="left:636px;top:2732px;width:118px;height:14px;border-radius:7px"></div>
<div class="abs partner" style="left:815px;top:2725px;width:110px;height:26px;border-radius:4px;background:#8fc9e6"></div>
<div class="abs partner" style="left:990px;top:2725px;width:92px;height:28px;border-radius:4px"></div>

<footer class="abs footer"></footer>
<h6 class="abs foot-h" style="left:147px">CONTACT US</h6>
<div class="abs foot-line" style="left:147px;top:2960px">
  <svg width="18" height="22" viewBox="0 0 18 22"><path d="M9 1a7 7 0 0 1 7 7c0 5-7 13-7 13S2 13 2 8a7 7 0 0 1 7-7z" fill="#f05423"/><circle cx="9" cy="8" r="2.5" fill="#151515"/></svg>
  <span>Your Address Goes Here</span>
</div>
<div class="abs foot-line" style="left:147px;top:3020px">
  <svg width="18" height="18" viewBox="0 0 18 18"><path d="M4 1l3 4-2 2c1 2 4 5 6 6l2-2 4 3-2 3C8 17 1 10 1 4z" fill="#f05423"/></svg>
  <span>+0123 456 789</span>
</div>
<div class="abs foot-line" style="left:147px;top:3060px">
  <svg width="18" height="14" viewBox="0 0 18 14"><rect width="18" height="14" rx="1" fill="#f05423"/><path d="M1 1l8 7 8-7" fill="none" stroke="#151515" stroke-width="1.5"/></svg>
  <span>Youremailaddressgoeshere</span>
</div>
<div class="abs" style="left:147px;top:3104px;display:flex;gap:8px"><span style="width:20px;height:20px;border-radius:50%;background:#bbb"></span><span style="width:20px;height:20px;border-radius:50%;background:#bbb"></span></div>

<h6 class="abs foot-h" style="left:441px">CUSTOMER SERVICE</h6>
<ul class="abs foot-list" style="left:441px;top:2958px">
  <li>Lorem Ipsum</li><li>Lorem Ipsum</li><li>Lorem Ipsum</li><li>Lorem Ipsum</li><li>Lorem Ipsum</li><li>Lorem Ipsum</li><li>Lorem Ipsum</li>
</ul>

<h6 class="abs foot-h" style="left:678px">QUICK LINKS</h6>
<ul class="abs foot-list" style="left:678px;top:2958px">
  <li>Faq</li><li>New</li><li>About Us</li><li>Privacy Policy</li><li>Terms of Use</li>
</ul>

<h6 class="abs foot-h" style="left:885px">NEWS LETTER SIGN UP</h6>
<div class="abs" style="left:863px;top:2960px;font-size:14px">Subscribe to our News Letter</div>
<div class="abs news-input">E-mail</div>
<svg class="abs" style="left:872px;top:3003px" width="16" height="11" viewBox="0 0 16 11"><rect width="16" height="11" fill="#777"/><path d="M1 1l7 5 7-5" fill="none" stroke="#bdbdbd" stroke-width="1.2"/></svg>
<div class="abs subscribe">Subscribe</div>

<div class="abs bottom-bar">
  HOME | SITE MAP | POLICIES | ARTICLES | CONTACT US | PRINT THIS PAGE | RSS rss | TOP OF PAGE<br>
  COPYRIGHT © 2016 meridel falls
</div>

</body>
</html>
```